Korveth Signal Works DL Promo Flyer

This DL flyer is targeted at the corporate / business sector to promote our products and services to the professional market. Photos are worth a 1000 words hence they are intended to grasp initial interest. We would like the brochure to exceptionally high standard, reflect the high technology market we operate within yet be simple to understand. In the attached draft the text component is ideal but the layout and placement needs work, it needs an eye-catching front page. I would envisage a shaded image behind the texts and photos, the manufacturer logos could be shaded or remain as colour if not too distracting, just after a professional eye-catching design. have attached a draft and images that can be used, also need to fill in one panel with something and willing to discuss options there.

Target Market(s)

Corporate & Government sectors

Industry/Entity Type

Business

Font styles to use
Sans Serif

Colors
0355a3

Requirements
Must have
• Eye-catching, professional design and reflect the technology market we operate within. The brochure will be printed on high-gloss card opposed to paper to give it a professional appearance and hopefully assist in making it past the receptionist to the decision makers and purchasers. also Promote the fact we are a national company, Australian owned.
Nice to have
• Impressive photos - worth a thousand words - stunning front page that makes people want to open the brochure and know what it is.
Should not have
• Be cluttered and difficult to follow

```html
<!DOCTYPE html>
<html lang="en">
<head>
<meta charset="utf-8">
<title>Korveth Signal Works – DL Flyer</title>
<link rel="stylesheet" href="https://fonts.googleapis.com/css2?family=Open+Sans:ital,wght@0,400;0,600;0,700;1,400&display=swap">
<style>
:root{
  --bg:#8e8f91;
  --paper:#ffffff;
  --teal:#1598b4;
  --blue:#0355a3;
  --ink:#2b2d30;
  --muted:#55595e;
  --photo-dark:#3a3f55;
  --photo-warm:#8a6a4a;
}
*{margin:0;padding:0;box-sizing:border-box}
html,body{width:1200px;height:900px;overflow:hidden}
body{background:radial-gradient(circle at 50% 45%,#a7a8aa,var(--bg));font-family:"Open Sans",sans-serif;color:var(--ink)}
.flyer{position:absolute;left:30px;top:47px;width:1140px;height:806px;background:var(--paper);display:flex;box-shadow:0 12px 30px rgba(0,0,0,.35)}
.panel{position:relative;width:380px;height:100%;padding:40px 22px 20px;font-size:7.4px;line-height:1.4}
.panel + .panel{border-left:1px solid #e4e6e8}
.band{position:absolute;left:0;top:0;width:100%;height:26px;background:var(--teal)}
.photo{border:2px solid var(--blue);background:linear-gradient(135deg,var(--photo-dark),#6a7390 60%,#c9c3b8)}
.photo.warm{background:linear-gradient(135deg,#5a1f24,#a83a3a 50%,#e0b69a)}
.photo.room{background:linear-gradient(160deg,#d9d4c8,var(--photo-warm) 70%,#4a3a2a)}
.photo.hall{background:linear-gradient(160deg,#cfe0ec,#6d8eaa 60%,#2a3a4a)}
.caption{color:var(--blue);font-style:italic;font-size:7px;text-align:center;margin-top:2px}
.row{display:flex;gap:10px;margin-bottom:10px}
.row .photo{flex:0 0 120px;height:80px}
h2{color:var(--blue);font-weight:400;font-size:15px;margin:10px 0 5px}
h3{color:var(--blue);font-style:italic;font-weight:600;font-size:9px;margin:6px 0 3px}
ul{list-style:none}
li::before{content:"› ";color:var(--blue)}
.logos{position:absolute;left:18px;right:18px;bottom:16px;display:flex;flex-wrap:wrap;gap:6px 12px;align-items:center;justify-content:center}
.logos span{font-weight:700;color:var(--blue);font-size:11px}
.logos.big span{font-size:17px}
.cols{display:flex;gap:12px}
.cols ul{flex:1}
.values{color:var(--teal);font-style:italic;text-align:center;font-size:7.4px;margin:6px 0}
.contact{text-align:center;color:var(--blue);font-weight:600;font-size:9px;margin-top:8px}
.cover{padding:0}
.cover svg{position:absolute;left:0;top:0}
.brand{display:flex;align-items:center;gap:10px;font-size:26px;font-weight:400}
.brand i{display:block;width:30px;height:30px;background:var(--teal)}
.brand.on-photo{position:absolute;left:150px;top:50px;color:#fff;font-size:20px}
.brand.on-photo i{width:24px;height:24px}
.brand.main{position:absolute;left:48px;top:470px;color:var(--ink)}
.offices{position:absolute;left:48px;top:540px;font-size:8px;line-height:1.45}
.offices b{display:block;margin-top:6px;font-weight:600}
</style>
</head>
<body>
<div class="flyer">

  <section class="panel profile">
    <div class="band"></div>
    <div class="row">
      <div>
        <div class="photo" style="width:120px;height:70px" role="img" aria-label="Boardroom with video conferencing screen"></div>
        <div class="caption">/Company Profile/</div>
      </div>
      <p>Korveth Signal Works are a dedicated team of audio visual professionals whose customer focus, expertise and purchasing power result in outstanding presentation solutions that offer state-of-the-art technology combined with reliability and value for money to our customers. With offices in Melbourne, Brisbane, Sydney and Perth, we design strategic options to meet your unique needs to deliver the optimal communications environments that simply work.</p>
    </div>
    <div class="row">
      <div>
        <div class="photo warm" role="img" aria-label="Function room with presentation screens"></div>
        <div class="caption">/ Connecting People with Technology /</div>
      </div>
      <p>As an authorised reseller of over 500 different audio visual product lines, we are able to provide you with the best solution and equipment to meet your needs. The stringent selection process we follow ensures all items we support are reliable and suited to the job they have been specified for.</p>
    </div>
    <div class="row">
      <div class="photo room" role="img" aria-label="Training room with projection screen"></div>
      <ul>
        <li>Lighting and Power Switching</li>
        <li>Architectural Lighting Control System Integration</li>
        <li>240V Load Control (Curtains, Blinds, Lighting)</li>
        <li>Production, Effects and Themed Lighting</li>
        <li>Infrastructure Platforms</li>
      </ul>
    </div>
    <h3>/ Who we are /</h3>
    <ul>
      <li>Cat 5e and Cat 6 Distribution for Data</li>
      <li>Public and/or Private Wireless Networking and Internet Distribution</li>
      <li>Security Cabling and CCTV Monitoring</li>
      <li>Fixed and Pan, Tilt, Zoom Camera Systems</li>
    </ul>
    <p style="margin-top:4px">The business was established in 2000 with offices across the country. Our national and global organisations deliver a complete, consistent and reliable audio visual integration and service expertise to a wide range of industries, including Corporate, Government, Education, Health, Hospitality, Houses of Worship and Aerospace &amp; Defence.</p>
    <h2>/ Code of conduct /</h2>
    <p>We are committed to acting with integrity at all times. Our success is dependent on the way our people conduct themselves every day. The Code of Conduct is a commitment to performance with integrity and defines the standards of ethical conduct that all employees must follow. We will not condone activity that fails to meet these minimum standards.</p>
    <div class="logos">
      <span>Sonvale</span><span>Orrin</span><span>Kaldo</span><span>Veltro</span><span>Quorix</span><span>Brandt</span>
    </div>
  </section>

  <section class="panel services">
    <div class="band"></div>
    <div class="row">
      <p>As a national company we draw on the expertise of our system designers and project managers across Australia to provide innovative audio visual solutions. That means you will always receive the benefits of our experienced national network, integrating multiple elements from the following areas of expertise.</p>
      <div class="photo hall" style="flex:0 0 90px;height:60px" role="img" aria-label="Meeting room with display"></div>
    </div>
    <p>By providing a unique business environment, our staff are highly motivated and stay up to date with current technologies and services via regular external and internal training programmes, putting knowledge and ideas into practice.</p>
    <div class="row" style="margin-top:8px">
      <div style="flex:1">
        <div class="photo hall" style="height:72px" role="img" aria-label="Foyer with video wall"></div>
        <div class="caption">/ Making a difference in a changing world /</div>
      </div>
      <div style="flex:1">
        <div class="photo" style="height:72px" role="img" aria-label="Conference room with projection"></div>
        <div class="caption">/ What we do /</div>
      </div>
    </div>
    <div class="cols">
      <ul>
        <li>AV Control Systems</li><li>Commercial Control Integration</li><li>Control System Software Architecture</li><li>Multiple Technology Integration</li><li>Paging and Public Address</li><li>Background Music</li><li>Multiroom Audio Distribution</li><li>Conferencing Systems</li><li>Interactive LED/LCD Touch Screens</li><li>Video Conferencing</li><li>Large Screen Display Systems</li><li>Digital Signage Solutions</li>
      </ul>
      <ul>
        <li>Master Antenna Television</li><li>Installation, Support &amp; Managed Services</li><li>Free To Air Digital TV Distribution</li><li>Cable Amplified TV</li><li>Fibre Optic Distribution</li><li>Digital Signage Channels</li><li>Audio Visual Design Consultancy</li><li>AV Project Management</li><li>Preventative maintenance agreements</li><li>Installation of audio visual hardware</li>
      </ul>
    </div>
    <h2>/ Core values /</h2>
    <p>Our increasingly complex environment makes it essential that we deliver clear value to our clients and continue to have clarity in our own values. Our values define who we are and what we stand for. An ethical mindset supports decision-making in the course of our daily lives, for our clients and the communities in which we live and work.</p>
    <p class="values">Leading by example / Working together / Communicating openly and honestly / Being committed to our clients / Acting with integrity / Delivering what we promise</p>
    <div class="contact">1300 555 019<br>www.korvethsignal.com.au<br>info@korvethsignal.com.au<br>MELBOURNE · SYDNEY · BRISBANE · PERTH</div>
    <div class="logos big">
      <span>Linkpanel</span><span>Norvex</span><span>Tamaru</span>
    </div>
  </section>

  <section class="panel cover">
    <svg width="380" height="420" viewBox="0 0 380 420" role="img" aria-label="Reception desk with large video wall">
      <defs>
        <clipPath id="cover-clip"><circle cx="340" cy="120" r="290"/></clipPath>
        <linearGradient id="cover-tone" x1="0" y1="0" x2="0" y2="1">
          <stop offset="0" stop-color="#d8b98e"/>
          <stop offset=".35" stop-color="#4a3a30"/>
          <stop offset=".7" stop-color="#7d6a58"/>
          <stop offset="1" stop-color="#e4dcd2"/>
        </linearGradient>
      </defs>
      <rect width="380" height="420" fill="url(#cover-tone)" clip-path="url(#cover-clip)"/>
      <circle cx="340" cy="120" r="290" fill="none" stroke="#0355a3" stroke-width="3"/>
    </svg>
    <div class="brand on-photo"><i></i>Korveth Signal Works</div>
    <div class="brand main"><i></i>Korveth Signal Works</div>
    <div class="offices">
      <b>/ Victoria /</b>12/80 Larkwood Rd, Elmsbury, VIC 3170, Australia<br>P: 03 9555 0142 | F: 03 9555 0143
      <b>/ New South Wales /</b>Level 2, 210 Marlow Rd, Fernhill, NSW 2045, Australia<br>P: 02 9555 0310 | F: 02 9555 0311
      <b>/ Queensland /</b>3/14 Quill St, Redmount, QLD 4058, Australia<br>P: 07 3555 0227 | F: 07 3555 0228
      <b>/ Western Australia /</b>57 Tamber Street, Westbrook, WA 6019, Australia<br>P: 08 9555 0473 | F: 08 9555 0474
    </div>
    <div class="logos big">
      <span>Celvane</span><span>Ridgeway</span><span>Halvor</span>
    </div>
  </section>

</div>
</body>
</html>
```